Business Card Design

My business is writing crime novels to entertain readers. I write legal thrillers and mysteries. I need a card for publishers, agents, other authors, and media.

Industry/Entity Type

Legal

Contact Information for Business Card

Paul Trenholt
www.trenholtnoir.example
pbtrenholt@mailbox.example
0064 27 5170942

```html
<!DOCTYPE html>
<html lang="en">
<head>
<meta charset="utf-8">
<title>Paul Trenholt – Business Card</title>
<link rel="stylesheet" href="https://fonts.googleapis.com/css2?family=Felipa&display=swap">
<style>
  :root {
    --page-bg: #2a2826;
    --card-black: #000000;
    --card-gloss: #3a3a3a;
    --card-lower: #0b0b0b;
    --title-ink: #dcdcdc;
    --contact-ink: #b4b4b4;
    --portrait-light: #6e5d55;
    --portrait-mid: #2b2624;
    --portrait-dark: #050505;
  }
  html, body {
    margin: 0;
    padding: 0;
    width: 1200px;
    height: 758px;
    overflow: hidden;
    background: var(--page-bg);
  }
  .card {
    position: absolute;
    left: 40px;
    top: 69px;
    width: 1120px;
    height: 620px;
    border-radius: 18px;
    overflow: hidden;
    background: var(--card-black);
    font-family: "Felipa", serif;
  }
  .card__gloss {
    position: absolute;
    inset: 0;
    width: 100%;
    height: 100%;
  }
  .card__portrait {
    position: absolute;
    left: 567px;
    top: 60px;
    width: 486px;
    height: 560px;
    border-radius: 200px 200px 0 0;
    background: radial-gradient(ellipse 55% 60% at 50% 38%, var(--portrait-light) 0%, var(--portrait-mid) 55%, var(--portrait-dark) 100%);
  }
  .card__title {
    position: absolute;
    left: 47px;
    top: 338px;
    margin: 0;
    font-weight: 400;
    font-size: 64px;
    line-height: 1;
    color: var(--title-ink);
    white-space: nowrap;
  }
  .card__contact {
    position: absolute;
    left: 47px;
    margin: 0;
    font-size: 32px;
    line-height: 1;
    color: var(--contact-ink);
    white-space: nowrap;
  }
  .card__contact--email { top: 433px; }
  .card__contact--phone { top: 484px; }
  .card__contact--web   { top: 537px; }
</style>
</head>
<body>
  <div class="card">
    <svg class="card__gloss" viewBox="0 0 1120 620" preserveAspectRatio="none" aria-hidden="true">
      <defs>
        <linearGradient id="lowerFade" x1="0" y1="0" x2="0" y2="1">
          <stop offset="0" stop-color="var(--card-gloss)"/>
          <stop offset="0.12" stop-color="var(--card-lower)"/>
          <stop offset="1" stop-color="var(--card-black)"/>
        </linearGradient>
      </defs>
      <path d="M0 118 C 250 80, 520 88, 760 115 C 900 130, 1020 112, 1120 96 L1120 620 L0 620 Z" fill="url(#lowerFade)"/>
    </svg>
    <div class="card__portrait" role="img" aria-label="Portrait photograph of the author in a dark leather jacket and white shirt"></div>
    <h1 class="card__title">Author: Paul Trenholt</h1>
    <p class="card__contact card__contact--email">E-mail: pbtrenholt@mailbox.example</p>
    <p class="card__contact card__contact--phone">Phone: 0064 27 5170942</p>
    <p class="card__contact card__contact--web">www.trenholtnoir.example</p>
  </div>
</body>
</html>
```